Tolvik service sheets and folder

A set of 12 Service sheets plus a rate card to be inserted into a folder - each to be designed and formatted.
A4
Portrait
- the idea is to keep things simple and crisp.
I would use the logo (see attached .ai file) at the top and maybe an separate image to go with each sheet

Around 350 words per page (see attached example)
The format is mainly text and bullet points, but each page will be same layout (just a different image as indicated above).

Need to factor in a folder to hold the service sheets.

The documents to have a good sales impact and your experience and advice on best ideas would be welcome. The key is to keep it crisp, elegant & professional for financial services.

The output files should be in PDF and raw file formats so that printing can be managed easily in future., Details for my new Catalogue Design Project will be added soon.

Industry/Entity Type

Financial

Requirements
Must have
• Inspire us!
Should not have
• No images of people or parts (like hands, arms) etc

```html
<!DOCTYPE html>
<html lang="en">
<head>
<meta charset="utf-8">
<title>Tolvik service sheet and folder</title>
<link rel="stylesheet" href="https://fonts.googleapis.com/css2?family=Questrial&display=swap">
<style>
  :root {
    --backdrop: #e9e6e1;
    --paper: #ffffff;
    --paper-shade: #f1f1f1;
    --ink: #1d1d1d;
    --ink-soft: #4a4a4a;
    --band: #111111;
    --leaf-green: #6a9e3a;
    --signal-red: #e2231a;
    --pocket-grey: #dcdcdc;
    --photo-light: #dfe8f2;
    --photo-blue: #6f9cc8;
  }
  * { box-sizing: border-box; margin: 0; padding: 0; }
  html, body { width: 1200px; height: 542px; overflow: hidden; }
  body {
    background: var(--backdrop);
    font-family: "Questrial", "Century Gothic", sans-serif;
    color: var(--ink);
    position: relative;
  }

  /* Folder */
  .folder { position: absolute; left: 110px; top: 14px; width: 560px; height: 514px; }
  .folder-cover {
    position: absolute; left: 0; top: 0; width: 560px; height: 370px;
    background: linear-gradient(90deg, var(--paper-shade), var(--paper) 30%, var(--paper-shade) 50%, var(--paper) 80%);
    box-shadow: 0 1px 3px rgba(0,0,0,.2);
    overflow: hidden;
  }
  .folder-spine { position: absolute; left: 280px; top: 0; width: 1px; height: 370px; background: #cfcfcf; }
  .cover-waves { position: absolute; left: 0; bottom: 0; }
  .back-contact {
    position: absolute; left: 12px; top: 290px; color: #fff; font-size: 8px; line-height: 13px;
  }
  .back-contact .icon { display: inline-block; vertical-align: middle; margin-right: 4px; }
  .back-contact .address { margin-top: 8px; }
  .front-name {
    position: absolute; left: 378px; top: 140px; font-size: 34px; letter-spacing: 1px; color: var(--ink);
  }
  .front-name .dot {
    display: inline-block; width: 22px; height: 22px; border-radius: 50%;
    background: var(--signal-red); margin-right: 10px; vertical-align: 2px;
  }
  .front-web {
    position: absolute; left: 280px; width: 280px; top: 317px; text-align: center;
    font-size: 10px; letter-spacing: 2.5px; color: var(--ink-soft);
  }
  .pocket {
    position: absolute; top: 372px; width: 279px; height: 140px;
    display: flex; align-items: center; justify-content: center;
    font-size: 22px; letter-spacing: 1px;
  }
  .pocket-left {
    left: 0; background: linear-gradient(90deg, #cfcfcf, var(--paper) 45%, var(--pocket-grey));
    border-radius: 0 0 0 0; clip-path: polygon(0 0, 100% 10%, 100% 100%, 4% 100%, 0 92%);
    color: var(--ink);
  }
  .pocket-right {
    left: 281px; background: var(--leaf-green); color: var(--paper);
    clip-path: polygon(0 10%, 100% 0, 100% 92%, 96% 100%, 0 100%);
  }

  /* Service sheet */
  .service-sheet {
    position: absolute; left: 740px; top: 16px; width: 360px; height: 510px;
    background: var(--paper); box-shadow: 0 1px 4px rgba(0,0,0,.25); overflow: hidden;
  }
  .sheet-name { position: absolute; right: 16px; top: 22px; font-size: 14px; letter-spacing: .5px; }
  .sheet-title { position: absolute; left: 0; right: 0; top: 48px; text-align: center; font-size: 16px; font-weight: 400; }
  .sheet-photo {
    position: absolute; left: 26px; top: 72px; width: 308px; height: 126px;
    background: linear-gradient(120deg, var(--photo-light), #f4f7fb 45%, var(--photo-blue));
  }
  .sheet-caption { position: absolute; left: 26px; right: 26px; top: 204px; text-align: center; font-size: 6.5px; color: var(--ink-soft); }
  .sheet-body { position: absolute; left: 26px; right: 26px; top: 220px; font-size: 6.6px; line-height: 8.6px; color: var(--ink-soft); text-align: justify; }
  .sheet-body p { text-indent: 16px; margin-bottom: 8px; }
  .sheet-waves { position: absolute; left: 0; bottom: 0; }
  .sheet-contact { position: absolute; left: 10px; bottom: 8px; color: #fff; font-size: 5px; line-height: 8px; }
  .sheet-contact .address { margin-top: 4px; }
  .sheet-web { position: absolute; right: 40px; bottom: 12px; font-size: 6px; letter-spacing: 1.5px; color: var(--ink-soft); }
</style>
</head>
<body>

<section class="folder" aria-label="Presentation folder">
  <div class="folder-cover">
    <svg class="cover-waves" width="560" height="370" viewBox="0 0 560 370">
      <path d="M0,280 C140,282 250,330 420,338 C480,341 530,336 560,334 L560,370 L0,370 Z" fill="var(--band)"/>
      <path d="M0,274 C140,276 250,324 420,332 C480,335 530,330 560,327" fill="none" stroke="var(--leaf-green)" stroke-width="3"/>
      <path d="M290,356 C380,352 470,346 560,338 L560,344 C470,352 380,358 290,360 Z" fill="var(--signal-red)"/>
    </svg>
    <div class="folder-spine"></div>

    <div class="back-contact">
      <div><svg class="icon" width="7" height="7" viewBox="0 0 10 10"><path d="M2 1 L4 1 L5 3.5 L3.8 4.5 C4.5 6 5.5 7 6.5 7.2 L7.5 6 L10 7 L10 9 C5 10 0 5 1 1 Z" fill="var(--signal-red)"/></svg>+44 (0) 20 7946 0321</div>
      <div><svg class="icon" width="7" height="6" viewBox="0 0 10 8"><rect width="10" height="8" fill="var(--signal-red)"/><path d="M0 0 L5 4.5 L10 0" fill="none" stroke="#fff" stroke-width="1"/></svg>info@tolvik.com</div>
      <div class="address">12 Harrow Row, London, EC1A 9QT</div>
    </div>

    <div class="front-name"><span class="dot"></span>TOLVIK</div>
    <div class="front-web">www.tolvik.com</div>
  </div>

  <div class="pocket pocket-left">TOLVIK</div>
  <div class="pocket pocket-right">TOLVIK</div>
</section>

<article class="service-sheet" aria-label="Service sheet">
  <div class="sheet-name">TOLVIK</div>
  <h1 class="sheet-title">Investment Management Services</h1>
  <div class="sheet-photo" role="img" aria-label="Photo of financial charts and reports on a desk"></div>
  <p class="sheet-caption">Simplifying investing; with your portfolio managed by professionals</p>
  <div class="sheet-body">
    <p>A bespoke service tailored to your needs, with a dedicated investment manager taking over the burden of monitoring and managing your portfolio of investments.</p>
    <p>The Discretionary Investment Management Service passes the burden of managing your portfolio of investments to a dedicated investment manager. Investments are targeted to provide the best returns matched to your stated risk profile and investment objectives. Your investment manager is available to discuss any aspect of your investments and you will be regularly updated with the performance of your portfolio.</p>
    <p>Our role is to assist investors acquire a stake in the world economy through diversified portfolios. Investment processes blend our strategic view, a tactical overlay, an asset allocation policy and research of individual investment opportunities on a long term basis. We do not confine ourselves to a particular methodology, but we look for value, using such traditional measures as yield, price to book and the discounted value of cash flows. We aim to invest in companies that grow their dividends in the belief that an increasing income supports capital values.</p>
  </div>
  <svg class="sheet-waves" width="360" height="60" viewBox="0 0 360 60">
    <path d="M0,18 C90,20 170,44 270,48 C310,49 340,47 360,46 L360,60 L0,60 Z" fill="var(--band)"/>
    <path d="M0,14 C90,16 170,40 270,44 C310,45 340,43 360,42" fill="none" stroke="var(--leaf-green)" stroke-width="2"/>
    <path d="M180,56 C250,54 310,52 360,50 L360,53 C310,55 250,57 180,58 Z" fill="var(--signal-red)"/>
  </svg>
  <div class="sheet-contact">
    <div>+44 (0) 20 7946 0321</div>
    <div>info@tolvik.com</div>
    <div class="address">12 Harrow Row, London, EC1A 9QT</div>
  </div>
  <div class="sheet-web">www.tolvik.com</div>
</article>

</body>
</html>
```